Website Design Request - Management Consulting Firm

We need a Website designed for an IT Management Staffing and Recruiting firm called VANTREX based in San Francisco.

The firm is an high-end technology staffing agency. Our focus is on quality and high-caliber candidates rather than quantity.

The website will have two main home pages. One for the recruiter and another on for the candidates.

The website needs to optimize for mobile devices as well.

I have attached few mock-ups that I have done just to show what I am thinking. The UI needs to be very clean, fluid, and it needs to have a modern, rustic, professional feel to it.

Target Market(s)

Technology Manager, Director, VP, CIO of Companies that have $4b-10b dollar revenue. Such as hollowmeadowgoods.example , https://www.quillbarrow.example/, lumatic.example, zib.example

Industry/Entity Type

Management Consulting

Number of Pages Required

5+ page

Font styles to use
Sans Serif

Colors
f37122
ffffff

Requirements
Must have
• Please review mock-ups for suggestions
Nice to have
Should not have

```html
<!DOCTYPE html>
<html lang="en">
<head>
<meta charset="utf-8">
<title>VANTREX — Employers</title>
<link rel="stylesheet" href="https://fonts.googleapis.com/css2?family=Source+Sans+3:wght@300;400;600&display=swap">
<style>
  :root {
    --orange: #f37122;
    --orange-dark: #d2591c;
    --white: #ffffff;
    --ink: #2b2b2b;
    --grey: #777777;
    --text: #444444;
    --card-tint: #fdeee6;
    --card-line: #f6c9b0;
    --hero-dark: #2a2623;
  }
  * { box-sizing: border-box; margin: 0; padding: 0; }
  html, body { width: 960px; height: 1200px; overflow: hidden; background: var(--white); }
  body { position: relative; font-family: "Source Sans 3", "Source Sans Pro", sans-serif; color: var(--ink); }

  .site-header { position: absolute; top: 0; left: 0; width: 960px; height: 79px; background: var(--white); }
  .brand { position: absolute; left: 97px; top: 24px; display: flex; align-items: center; gap: 6px;
    font-size: 24px; font-weight: 600; color: var(--orange); letter-spacing: 1px; }
  .brand-dot { width: 10px; height: 10px; border-radius: 50%; background: var(--orange); }
  .main-nav a { position: absolute; top: 31px; font-size: 14.5px; font-weight: 300; color: var(--grey); text-decoration: none; }
  .main-nav .nav-pros { left: 253px; }
  .main-nav .nav-employers { left: 359px; color: var(--orange); font-weight: 400; }
  .login { position: absolute; left: 741px; top: 34px; font-size: 11px; font-weight: 300; color: var(--grey); }
  .signup { position: absolute; left: 784px; top: 29px; width: 80px; height: 24px; border-radius: 12px;
    background: var(--ink); color: var(--white); font-size: 11px; line-height: 24px; text-align: center; }

  .hero { position: absolute; top: 79px; left: 0; width: 960px; height: 512px;
    background: linear-gradient(100deg, #3a3532 0%, #2f2b28 35%, #5a4330 62%, #4a3322 80%, #2e2621 100%); }
  .hero-photo { position: absolute; inset: 0; }
  .hero h1 { position: absolute; left: 96px; top: 124px; font-size: 38px; font-weight: 600; color: var(--white); }
  .hero .lead { position: absolute; left: 96px; top: 170px; font-size: 19px; color: var(--white); }
  .signup-form { position: absolute; left: 97px; top: 217px; display: flex; }
  .signup-form .field { width: 380px; height: 40px; background: var(--white); border-radius: 3px 0 0 3px;
    padding-left: 14px; font-size: 18px; font-weight: 300; line-height: 40px; color: #9a9a9a; }
  .signup-form .cta { width: 112px; height: 40px; background: var(--orange); border-radius: 0 3px 3px 0;
    color: var(--white); font-size: 14px; font-weight: 600; line-height: 40px; text-align: center; }
  .terms { position: absolute; left: 96px; top: 270px; font-size: 9px; color: var(--white); }
  .terms span, .job-pitch span { color: var(--orange); }
  .job-title { position: absolute; left: 0; width: 960px; top: 410px; text-align: center;
    font-size: 19px; font-weight: 300; color: var(--white); }
  .job-pitch { position: absolute; left: 0; width: 960px; top: 439px; text-align: center;
    font-size: 14px; font-weight: 300; color: var(--white); }

  .tabs { position: absolute; top: 591px; left: 0; width: 960px; height: 48px; background: var(--orange); }
  .tab { position: absolute; top: 0; width: 256px; height: 48px; line-height: 48px; text-align: center;
    font-size: 14px; font-weight: 300; color: var(--white); }
  .tab.active { background: var(--orange-dark); font-weight: 400; }

  .focus-heading { position: absolute; top: 680px; left: 0; width: 1040px; text-align: center;
    font-size: 19px; font-weight: 300; color: var(--orange); }
  .card { position: absolute; top: 738px; width: 256px; height: 384px; }
  .card.highlight { background: var(--card-tint); border: 1px solid var(--card-line); }
  .card-photo { position: absolute; top: 38px; width: 160px; height: 160px; border-radius: 50%; }
  .card h3 { position: absolute; top: 218px; font-size: 14px; font-weight: 400; color: var(--orange); text-align: center; }
  .card ul { position: absolute; top: 253px; width: 170px; list-style: none; }
  .card li { font-size: 10.5px; font-weight: 300; line-height: 13.6px; color: var(--text); margin-bottom: 5px; }
</style>
</head>
<body>
  <header class="site-header">
    <div class="brand"><span>VANTREX</span><span class="brand-dot"></span></div>
    <nav class="main-nav">
      <a class="nav-pros" href="#">Professionals</a>
      <a class="nav-employers" href="#">Employers</a>
    </nav>
    <span class="login">Log In</span>
    <span class="signup">Sign Up</span>
  </header>

  <section class="hero">
    <div class="hero-photo" role="img" aria-label="Business professional in a suit seated with a laptop and a leather briefcase, darkened"></div>
    <h1>Hire Top IT Project Management Talents</h1>
    <p class="lead">Search our network, shortlist candidates, send interview requests &amp; fill positions fast</p>
    <div class="signup-form">
      <div class="field">Your Business Email Address...</div>
      <div class="cta">Get Started</div>
    </div>
    <p class="terms">By entering your email address, you agree to our <span>Terms &amp; Conditions</span></p>
    <p class="job-title">Looking for a job?</p>
    <p class="job-pitch"><span>Upload Resume</span> and let companies send you offers.</p>
  </section>

  <nav class="tabs">
    <div class="tab active" style="left:96px">Our Focus</div>
    <div class="tab" style="left:352px">Why us</div>
    <div class="tab" style="left:608px">How it works?</div>
  </nav>

  <h2 class="focus-heading">Lorem ipsum dolor sit amet, consectetur adipiscing elit</h2>

  <article class="card highlight" style="left:97px">
    <div class="card-photo" style="left:48px;background:radial-gradient(circle at 50% 40%,#e9e9e9,#bdbdbd)" role="img" aria-label="Project manager pinning notes to a white brick wall"></div>
    <h3 style="left:0;width:256px">Project Managers</h3>
    <ul style="left:48px">
      <li>Manage IT Projects, Programs and Portfolio from start to finish.</li>
      <li>Get your projects back on track with our highly vetted consultatnts.</li>
      <li>Conduct Project audits, lessons learned and post-mortem.</li>
    </ul>
  </article>

  <article class="card" style="left:352px">
    <div class="card-photo" style="left:48px;background:radial-gradient(circle at 50% 40%,#d8d8d6,#3d4a66)" role="img" aria-label="Hands holding a tablet showing charts"></div>
    <h3 style="left:0;width:256px">PMO Leadership</h3>
    <ul style="left:48px">
      <li>Stand up IT PMO office and project governance.</li>
      <li>Revamp or optimize exisiting IT Project Management Processes.</li>
      <li>Temporarily run IT PMO through our highly qualified PM Leaders.</li>
    </ul>
  </article>

  <article class="card" style="left:613px">
    <div class="card-photo" style="left:48px;background:radial-gradient(circle at 45% 45%,#dfe9e6,#6f9a94)" role="img" aria-label="Two people reviewing paper charts beside a laptop keyboard"></div>
    <h3 style="left:0;width:262px">PM Trainer &amp; Coaches</h3>
    <ul style="left:48px">
      <li>Individual coaching or group project management training.</li>
      <li>Setup Project Portfolio Management Tools.</li>
      <li>Drive Project Management Governance and adoption.</li>
    </ul>
  </article>
</body>
</html>
```